Business Card Design

Business Card for professional consulting firm working with large financial institutions.

Target Market(s)

Executive buyers

Industry/Entity Type

Banking

Contact Information for Business Card

Mild creativity wanted. Not boring, but do elaborate artwork.

Font styles to use
Serif
Sans Serif

Colors

Designer to choose colors to be used in the design.

Requirements
Must have
• Standard business card features - company name, individual name, telephone, website, email, locations.
Nice to have
• Two colors
Should not have
• too many colors, fancy printing, cartoons.

```html
<!DOCTYPE html>
<html lang="en">
<head>
<meta charset="utf-8">
<title>Northvale Business Card</title>
<link href="https://fonts.googleapis.com/css2?family=Lato:wght@400;700;900&family=Noto+Serif:wght@400&display=swap" rel="stylesheet">
<style>
  :root {
    --stage: #2e2e2e;
    --paper: #f7f7f7;
    --paper-shade: #e4e4e4;
    --ink: #111111;
    --ink-soft: #8a8a8a;
    --swoosh: #bdbdbd;
    --band: #0b0b0b;
    --band-text: #d8d8d8;
  }
  * { margin: 0; padding: 0; box-sizing: border-box; }
  html, body { width: 1200px; height: 997px; overflow: hidden; }
  body {
    background: radial-gradient(ellipse at 50% 45%, #3a3a3a 0%, var(--stage) 60%, #1c1c1c 100%);
    font-family: "Lato", sans-serif;
    position: relative;
  }
  .card {
    position: absolute;
    left: 250px;
    width: 700px;
    height: 400px;
    background: linear-gradient(160deg, #ffffff 0%, var(--paper) 55%, var(--paper-shade) 100%);
    overflow: hidden;
    box-shadow: 0 18px 40px rgba(0,0,0,.55);
  }
  .card--back { top: 60px; }
  .card--front { top: 537px; }
  .card__band { position: absolute; left: 0; bottom: 0; width: 700px; height: 160px; }
  .brand {
    position: absolute;
    font-family: "Noto Serif", serif;
    color: var(--ink);
    font-weight: 400;
    display: flex;
    align-items: center;
    gap: 14px;
  }
  .brand__dot { width: 14px; height: 14px; border-radius: 50%; background: var(--ink-soft); }
  .card--back .brand { left: 0; right: 0; top: 120px; justify-content: center; font-size: 56px; color: #555; }
  .card--front .brand { left: 150px; top: 42px; font-size: 46px; }
  .tagline {
    position: absolute; left: 34px; bottom: 22px;
    color: var(--band-text); font-weight: 700; font-size: 20px; letter-spacing: .3px;
  }
  .person { position: absolute; right: 400px; top: 150px; text-align: right; }
  .person__name { font-weight: 900; font-size: 22px; letter-spacing: .5px; text-transform: uppercase; }
  .person__role { font-size: 17px; color: var(--ink-soft); margin-top: 2px; }
  .person__address { font-weight: 900; font-size: 19px; line-height: 1.3; margin-top: 12px; }
  .divider {
    position: absolute; left: 318px; top: 140px; width: 2px; height: 120px;
    background: linear-gradient(180deg, transparent, #555 50%, transparent);
  }
  .contacts { position: absolute; left: 346px; top: 150px; list-style: none; }
  .contacts li { display: flex; align-items: center; gap: 12px; font-size: 17px; height: 34px; color: var(--ink); }
  .contacts svg { width: 24px; height: 24px; flex: none; }
  .website {
    position: absolute; right: 34px; bottom: 54px;
    color: var(--band-text); font-size: 19px; letter-spacing: 1px;
  }
</style>
</head>
<body>

<section class="card card--back" aria-label="Card back">
  <svg class="card__band" viewBox="0 0 700 160" preserveAspectRatio="none" aria-hidden="true">
    <path d="M0 40 Q350 95 700 40 L700 160 L0 160 Z" fill="var(--swoosh)"/>
    <path d="M0 82 Q350 118 700 62 L700 160 L0 160 Z" fill="var(--band)"/>
  </svg>
  <div class="brand"><span class="brand__dot"></span>northvale</div>
  <p class="tagline">Strategitic Planning for your business</p>
</section>

<section class="card card--front" aria-label="Card front">
  <svg class="card__band" viewBox="0 0 700 160" preserveAspectRatio="none" aria-hidden="true">
    <path d="M0 150 Q420 120 700 10 L700 160 L0 160 Z" fill="var(--swoosh)"/>
    <path d="M0 160 Q430 140 700 40 L700 160 Z" fill="var(--paper)"/>
    <path d="M180 160 Q480 130 700 70 L700 160 Z" fill="var(--band)"/>
  </svg>
  <div class="brand"><span class="brand__dot"></span>northvale</div>

  <div class="person">
    <p class="person__name">Maren Holt</p>
    <p class="person__role">Development Manager</p>
    <p class="person__address">12/40 Harbour View Lane<br>Kelvin QLD 4101</p>
  </div>

  <div class="divider" aria-hidden="true"></div>

  <ul class="contacts">
    <li>
      <svg viewBox="0 0 24 24" aria-hidden="true"><circle cx="12" cy="12" r="12" fill="var(--ink)"/><path d="M7 9c0-1 1-2 5-2s5 1 5 2v1h-3V9h-4v1H7z M8 11h8l1 5H7z" fill="#fff"/></svg>
      +61 (0)400 123 456
    </li>
    <li>
      <svg viewBox="0 0 24 24" aria-hidden="true"><circle cx="12" cy="12" r="12" fill="var(--ink)"/><path d="M8 6h8v4H8z M6 10h12v6H6z M8 14h8v4H8z" fill="#fff"/></svg>
      +61 (0)7 3000 1234
    </li>
    <li>
      <svg viewBox="0 0 24 24" aria-hidden="true"><circle cx="12" cy="12" r="12" fill="var(--ink)"/><rect x="6" y="8" width="12" height="8" fill="#fff"/><path d="M6 8l6 5 6-5" stroke="var(--ink)" stroke-width="1.2" fill="none"/></svg>
      mholt@northvale.com
    </li>
  </ul>

  <p class="website">www.northvale.com</p>
</section>

</body>
</html>
```